www.tqhjobfinder.com RE-DESIGN with WordPress

We need to update our current site to WordPress and will also need to add several pages. We will not be very picky on the style and elements as long as the colors and logos are the same-- AL INFO ON SITE WILL STAY THE SAME...CURRENT SITE IS VERY OUTDATED.

The project will consist of using the current site as template (all pics, text etc) and then transferring all the info into a more up to date version. We will also need to add the following functions:

1.) Job Listings page of the current openings our recruitment agency is working on (Must be easily edited and changed) and will allow candidate to submit their resumes via a simple email link)

2.) Featured candidate page that highlights one of our current candidates (profile, pic, editable filed so we may paste bio (must be easily edited via word press.

3.) Bio Page of our current Recruiters (4 bios) - Editable so we can make changes

4.) ALL FINAL FILES MUST BE MIGRATED AND UPLOADED VIA THE DESIGNER SO WE CAN MAKE THE SITE.
Updates

Please make the "homepage" a scrolling page that include all the drop down menu categories using the same info on current site. We can edit or scale back the text if needed. Would, like to see new stock photos and photos must scale to fit all the way across screen and also be mobile and tablet friendly.

Target Market(s)

professional

Coding

Coded - Design and coding required

Font styles to use
Sans Serif

Colors
0355a3
ec1f27
000000
1b1b1b

Requirements
Must have
• All the current info on existing site www.tqhjobfinder.com
• Would like to have design with scolling home page such as:
• Did you get earlier message about the design I eliminated? I was hoping for site more like this?
• https://www.pivotlyhire.com/
• https://www.netgainly.com.au/lp/seo-analysis/
Nice to have
• Sleek masculine modern feel
Should not have
• No cursive

```html
<!DOCTYPE html>
<html lang="en">
<head>
<meta charset="utf-8">
<title>Tallis Quorum Hiring — Senior Level Executive Recruitment</title>
<link href="https://fonts.googleapis.com/css2?family=Open+Sans:wght@400;600;700&display=swap" rel="stylesheet">
<style>
:root{
  --red:#d21f26;
  --ink:#1b1b1b;
  --black:#000;
  --muted:#555;
  --light:#f0f0f0;
  --line:#d8d8d8;
  --blue:#0355a3;
  --white:#fff;
}
*{box-sizing:border-box;margin:0;padding:0}
html,body{width:1200px;height:3168px;overflow:hidden}
body{font-family:"Open Sans",Arial,sans-serif;color:var(--ink);background:var(--white);position:relative}
a{color:inherit;text-decoration:none}

.site-header{height:92px;position:relative}
.brand{position:absolute;left:56px;top:18px;display:flex;align-items:center;gap:10px}
.brand-dot{width:34px;height:34px;border-radius:50%;background:var(--red);flex:none}
.brand-name{font-size:22px;font-weight:700;color:var(--ink);line-height:1.05;width:200px}
.contact-bar{position:absolute;right:56px;top:14px;display:flex;gap:10px}
.contact-pill{display:flex;align-items:center;gap:6px;border:1px solid var(--line);border-radius:3px;padding:3px 9px;font-size:12px;color:var(--muted)}
.contact-pill svg{width:12px;height:12px}
.main-nav{position:absolute;right:56px;top:56px;display:flex;gap:26px;font-size:14px;font-weight:600}
.main-nav .current{color:var(--red)}

.hero{height:716px;position:relative;background:linear-gradient(180deg,#4a0c0e 0%,#a31a1f 38%,#b71d23 60%,#2a1010 100%);color:var(--white);text-align:center}
.hero-title{position:absolute;left:0;right:0;top:390px;font-size:46px;font-weight:700;line-height:1.22;text-shadow:0 2px 6px rgba(0,0,0,.35)}
.search-box{position:absolute;left:50%;top:548px;transform:translateX(-50%);width:360px;height:40px;background:var(--white);border-radius:3px;display:flex;align-items:center;justify-content:space-between;padding:0 14px;color:#888;font-size:13px}
.search-box svg{width:16px;height:16px}

.paths{position:relative;height:1076px}
.path-divider{position:absolute;left:600px;top:110px;width:1px;height:150px;background:var(--line)}
.path-title{position:absolute;top:128px;font-size:38px;font-weight:400;line-height:1.22;color:var(--ink)}
.path-photo{position:absolute;top:248px;height:420px;width:480px}
.card-heading{position:absolute;top:700px;font-size:16px;font-weight:700;line-height:1.3;padding-left:14px;border-left:5px solid var(--red)}
.card-text{position:absolute;top:752px;width:460px;font-size:12.5px;line-height:1.6;color:var(--muted)}
.learn-more{position:absolute;top:904px;font-size:12px;color:var(--red);font-weight:600}
.cta{position:absolute;top:960px;width:170px;height:36px;background:var(--red);color:var(--white);font-size:13px;font-weight:600;display:flex;align-items:center;justify-content:center;letter-spacing:.5px}

.about{position:absolute;top:1884px;left:0;width:1200px;height:384px;background:var(--light)}
.section-heading{position:absolute;font-size:18px;font-weight:700;line-height:1.25;padding-left:14px;border-left:5px solid var(--red)}
.social{position:absolute;display:flex;gap:8px}
.social span{width:22px;height:22px;border-radius:50%;background:var(--blue)}
.about-text{position:absolute;left:100px;top:168px;width:1000px;font-size:12.5px;line-height:1.7;color:var(--muted)}

.testimonials{position:absolute;top:2268px;left:0;width:1200px;height:556px}
.slider-arrows{position:absolute;right:100px;top:144px;display:flex;gap:10px;color:#999;font-size:22px}
.client-photo{position:absolute;left:100px;top:228px;width:140px;height:140px;border-radius:50%;background:linear-gradient(135deg,#c9b8a6,#6b5a4c)}
.quote{position:absolute;left:280px;top:220px;width:820px;font-size:13px;line-height:1.65;color:var(--muted)}
.quote-source{position:absolute;right:100px;top:380px;font-size:13px;font-weight:600;color:var(--ink)}

.site-footer{position:absolute;top:2824px;left:0;width:1200px;height:344px;background:var(--light)}
.footer-list{position:absolute;left:130px;top:116px;font-size:12.5px;line-height:1.6;color:var(--muted);list-style:none}
.footer-list li{display:flex;gap:8px;align-items:flex-start;margin-bottom:4px}
.footer-list svg{width:13px;height:13px;margin-top:3px;flex:none}
.follow{position:absolute;left:100px;top:240px;font-size:13px;font-weight:700}
.map-title{position:absolute;left:680px;top:30px;font-size:13px;font-weight:700}
.map{position:absolute;left:680px;top:56px;width:420px;height:196px;background:linear-gradient(135deg,#e4e2dc,#cfd6cf)}
.footer-nav{position:absolute;left:100px;top:304px;display:flex;gap:16px;font-size:11px;color:var(--muted)}
.footer-nav .current{color:var(--red)}
.copyright{position:absolute;right:100px;top:304px;font-size:11px;color:#888}
</style>
</head>
<body>

<header class="site-header">
  <a class="brand" href="#"><span class="brand-dot"></span><span class="brand-name">Tallis Quorum Hiring, Inc.</span></a>
  <div class="contact-bar">
    <span class="contact-pill"><svg viewBox="0 0 16 16" fill="none" stroke="#777" stroke-width="1.5"><rect x="1.5" y="3.5" width="13" height="9"/><path d="M1.5 3.5l6.5 5 6.5-5"/></svg>hello@tallisquorum-mail.com</span>
    <span class="contact-pill"><svg viewBox="0 0 16 16" fill="#777"><path d="M4 1.5l2.5 3-1.5 1.5c.8 2 2.5 3.7 4.5 4.5L11 9l3 2.5-1.5 2.5C7.5 14 2 8.5 2 3z"/></svg>555-014-2500</span>
  </div>
  <nav class="main-nav">
    <a class="current" href="#">Home</a><a href="#">About us</a><a href="#">Areas of Expertise</a><a href="#">Guarantee</a><a href="#">Testimonials</a><a href="#">Contact Us</a>
  </nav>
</header>

<section class="hero" role="img" aria-label="Photo of an executive team seated around a boardroom table, in deep red tones">
  <h1 class="hero-title">Senior Level Executive<br>Recruitement Consultants</h1>
  <div class="search-box"><span>Search Jobs</span><svg viewBox="0 0 16 16" fill="none" stroke="#555" stroke-width="1.8"><circle cx="6.5" cy="6.5" r="4.5"/><path d="M10 10l4.5 4.5"/></svg></div>
</section>

<section class="paths">
  <span class="path-divider"></span>
  <h2 class="path-title" style="left:100px">Searching for<br>Talent?</h2>
  <h2 class="path-title" style="left:640px">Searching for<br>a Job?</h2>
  <div class="path-photo" style="left:100px;background:linear-gradient(135deg,#d7d2cb,#6e6258)" role="img" aria-label="Photo of colleagues gathered around a laptop in a bright office"></div>
  <div class="path-photo" style="left:620px;background:linear-gradient(135deg,#3a3634,#1b1b1b)" role="img" aria-label="Photo of a professional in a suit seated at a desk"></div>

  <h3 class="card-heading" style="left:100px">What to Expect from<br>Your Executive Search Firm</h3>
  <p class="card-text" style="left:100px">An executive search involves a complex process that requires a substantial investment of your time and resources. When you hire a retained executive search firm, you're entitled to receive a high level of service. But what is the difference between a professional, reliable service and a lower quality of service? What are your rights and obligations as a client? Above all, how do you know when you have received excellence in client service?</p>
  <a class="learn-more" style="left:100px" href="#">Learn More</a>
  <a class="cta" style="left:250px" href="#">GET STARTED</a>

  <h3 class="card-heading" style="left:620px">For<br>Candidates</h3>
  <p class="card-text" style="left:620px">Aligning yourself with a top-tier executive search consultant can be one of the most important career decisions you will ever make. Let our team keep you informed about some of the most lucrative and satisfying career opportunities on the market today. We are in contact with thousands of senior level executives every year and work with the most dynamic and fulfilling organizations in the world.</p>
  <a class="learn-more" style="left:620px" href="#">Learn More</a>
  <a class="cta" style="left:776px" href="#">JOB OPENINGS</a>
</section>

<section class="about">
  <h2 class="section-heading" style="left:100px;top:100px">About<br>Tallis Quorum Hiring</h2>
  <div class="social" style="right:100px;top:108px"><span></span><span></span><span></span></div>
  <p class="about-text">Tallis Quorum Hiring is a nationally recognized executive search firm specializing in mid to senior level executive placement. Our areas of expertise range from Fortune 500 to start-up organizations searching for premier talent. Our candidates are industry leaders in their respective sectors and help us to make them aware of opportunities that will not only further their careers, but also fulfill their long-term goals. As a predominately retained executive search agency, we set the bar for excellence. As the only retained executive search agency that offers a 16-Year Guarantee on all searches, we exemplify the true qualities you look for in talent acquisition. Our philosophy centers on accountability, reliability, service and results. Tallis Quorum Hiring is the premier provider of executive human capital solutions, with services ranging from CEO recruitment to executive search, middle management recruitment and Leadership Development.</p>
</section>

<section class="testimonials">
  <h2 class="section-heading" style="left:100px;top:128px">Client<br>Testimonials</h2>
  <div class="slider-arrows"><span>&lsaquo;</span><span>&rsaquo;</span></div>
  <div class="client-photo" role="img" aria-label="Portrait photo of the client"></div>
  <blockquote class="quote">“The wealth of candidates presented to us was paramount in enabling us to maintain our particular hiring criteria, without compromise. The team was able to extract candidates that possess certain intangible qualities that fit perfectly with our corporate culture. Such candidates are taken through a thorough screening and qualification process by the firm before being presented to us for review, making our recruiting efforts seamless. The level of communication and representation received, while under a much accelerated timeline, was very impressive.”</blockquote>
  <p class="quote-source">CEO, Medical Diagnostic Company</p>
</section>

<footer class="site-footer">
  <div class="brand" style="left:100px;top:40px"><span class="brand-dot"></span><span class="brand-name">Tallis Quorum Hiring, Inc.</span></div>
  <ul class="footer-list">
    <li><svg viewBox="0 0 16 16" fill="#555"><path d="M8 1a5 5 0 0 0-5 5c0 4 5 9 5 9s5-5 5-9a5 5 0 0 0-5-5zm0 7a2 2 0 1 1 0-4 2 2 0 0 1 0 4z"/></svg><span>4820 Harbor Line Ave, Westport,<br>FL 33000</span></li>
    <li><svg viewBox="0 0 16 16" fill="#555"><path d="M4 1.5l2.5 3-1.5 1.5c.8 2 2.5 3.7 4.5 4.5L11 9l3 2.5-1.5 2.5C7.5 14 2 8.5 2 3z"/></svg><span>555-014-2500</span></li>
    <li><svg viewBox="0 0 16 16" fill="none" stroke="#555" stroke-width="1.5"><rect x="1.5" y="3.5" width="13" height="9"/><path d="M1.5 3.5l6.5 5 6.5-5"/></svg><span>hello@tallisquorum-mail.com</span></li>
  </ul>
  <p class="follow">Follow Us</p>
  <div class="social" style="left:100px;top:266px"><span></span><span></span><span></span></div>
  <p class="map-title">Our Location</p>
  <div class="map" role="img" aria-label="Street map showing the office location"></div>
  <nav class="footer-nav"><a class="current" href="#">Home</a><a href="#">About us</a><a href="#">Areas of Expertise</a><a href="#">Guarantee</a><a href="#">Testimonials</a><a href="#">Contact Us</a></nav>
  <p class="copyright">© 2018 Tallis Quorum Hiring, Inc. - All Rights Reserved</p>
</footer>

</body>
</html>
```